Velora Pedalworks

We are a new start up company selling (online) innovative cycling products.
Being a new player in the market a modern eye catching logo would be good.
Initially selling safety tail lights with blinkers & modern designed cycling gloves and eventually extending our range into cycling clothing. Many of our products will have a safety theme.

Please see logo attached.

Reason: I have extended deadline because i have just received the Logo to be used.

Target Market(s)

We will be target marketing to the young 20-30year old trendy commuter cyclists to the 40 - 60 year old weekend road riders with there immaculate color coordinated road bikes & clothing.

Industry/Entity Type

Safety

Requirements
Must have
• Name: Mavin Tolby
Line for Mobile No. 0438 261 905
Line for email Address: mavin@velorapedalworks.example.com.au
3 Lines for Postal Address: PO Box 3862
Wattle Crest Corner
NSW 2174
Website: www.velorapedalworks.example.com.au

```html
<!DOCTYPE html>
<html lang="en">
<head>
<meta charset="utf-8">
<title>Velora Pedalworks – Business Card</title>
<link rel="stylesheet" href="https://fonts.googleapis.com/css2?family=Lato:wght@400;700&display=swap">
<style>
  :root {
    --backdrop: #5a5a5a;
    --card-white: #ffffff;
    --brand-orange: #f26822;
    --ink: #1b1b1b;
    --divider: #111111;
    --on-orange: #ffffff;
  }
  * { box-sizing: border-box; margin: 0; padding: 0; }
  html, body {
    width: 1200px;
    height: 900px;
    overflow: hidden;
    background: var(--backdrop);
    font-family: "Lato", Arial, sans-serif;
  }
  .card {
    position: absolute;
    left: 100px;
    top: 164px;
    width: 1000px;
    height: 572px;
    background: var(--card-white);
    display: flex;
    flex-direction: column;
  }
  .card__brand {
    height: 256px;
    display: flex;
    align-items: center;
    justify-content: center;
    gap: 18px;
    padding-top: 30px;
  }
  .brand__dot {
    width: 34px;
    height: 34px;
    border-radius: 50%;
    background: var(--brand-orange);
  }
  .brand__name {
    font-size: 54px;
    font-weight: 700;
    color: var(--ink);
    letter-spacing: -0.5px;
  }
  .card__divider {
    height: 9px;
    background: var(--divider);
  }
  .card__details {
    flex: 1;
    background: var(--brand-orange);
    color: var(--on-orange);
    padding: 44px 56px 0 56px;
    display: flex;
    justify-content: space-between;
  }
  .person__name {
    font-size: 44px;
    font-weight: 400;
    text-transform: uppercase;
    letter-spacing: 0.5px;
    margin-bottom: 46px;
  }
  .person__surname { font-weight: 700; }
  .contact-list { list-style: none; }
  .contact-list li {
    display: flex;
    align-items: center;
    gap: 14px;
    font-size: 27px;
    line-height: 1.45;
  }
  .contact-icon {
    width: 28px;
    height: 28px;
    flex: none;
  }
  .postal {
    display: flex;
    gap: 16px;
    margin-top: 120px;
    font-size: 25px;
    line-height: 1.3;
  }
  .postal .contact-icon { width: 26px; height: 36px; margin-top: 2px; }
</style>
</head>
<body>
  <main class="card">
    <header class="card__brand">
      <span class="brand__dot"></span>
      <span class="brand__name">Velora Pedalworks</span>
    </header>
    <div class="card__divider"></div>
    <section class="card__details">
      <div class="person">
        <h1 class="person__name">Mavin <span class="person__surname">Tolby</span></h1>
        <ul class="contact-list">
          <li>
            <svg class="contact-icon" viewBox="0 0 28 28" aria-hidden="true">
              <rect x="1" y="1" width="26" height="26" rx="7" fill="#fff"/>
              <rect x="9" y="5" width="10" height="18" rx="2" fill="none" stroke="#1b1b1b" stroke-width="2"/>
              <circle cx="14" cy="19.5" r="1.2" fill="#1b1b1b"/>
            </svg>
            <span>0438 261 905</span>
          </li>
          <li>
            <svg class="contact-icon" viewBox="0 0 28 28" aria-hidden="true">
              <rect x="1" y="1" width="26" height="26" rx="7" fill="#fff"/>
              <rect x="6" y="8" width="16" height="12" fill="#1b1b1b"/>
              <path d="M6 8 L14 15 L22 8" fill="none" stroke="#fff" stroke-width="1.6"/>
            </svg>
            <span>mavin@velorapedalworks.example.com.au</span>
          </li>
          <li>
            <svg class="contact-icon" viewBox="0 0 28 28" aria-hidden="true">
              <circle cx="14" cy="14" r="13" fill="#fff"/>
              <rect x="6" y="12" width="9" height="5" rx="2.5" transform="rotate(-45 10.5 14.5)" fill="none" stroke="#1b1b1b" stroke-width="2"/>
              <rect x="13" y="11" width="9" height="5" rx="2.5" transform="rotate(-45 17.5 13.5)" fill="none" stroke="#1b1b1b" stroke-width="2"/>
            </svg>
            <span>www.velorapedalworks.example.com.au</span>
          </li>
        </ul>
      </div>
      <address class="postal" style="font-style: normal;">
        <svg class="contact-icon" viewBox="0 0 26 36" aria-hidden="true">
          <path d="M13 1 C6 1 1 6 1 13 C1 22 13 35 13 35 C13 35 25 22 25 13 C25 6 20 1 13 1 Z" fill="#fff"/>
          <circle cx="13" cy="13" r="4.5" fill="#f26822"/>
        </svg>
        <span>PO Box 3862<br>Wattle Crest Corner<br>NSW 2174</span>
      </address>
    </section>
  </main>
</body>
</html>
```